Medical Professionals- Financial services

We need a logo and stationery designed for a company called Vantorel Private Capital. Based in Queensland Australia, we provide financial services and planning for medical professionals. This includes all aspects of their financial life including Debt, Wealth accumulation, Risk management and ad hoc financial services including legal and accounting.

We do not have any specific requirements for stationery itself, anything that looks quite corporate would be great.

We need stationery for the following
- Business Cards- back
- With compliments
- Letter head
- Email signature
- Display folder
Updates

Please note there must be an accredited by QBL logo on all stationery

Must also include "Vantorel Private capital Authorised Representative of QBL Asset Advisory Pty Ltd AFS Licensee no. 418593"

EXCEPTIONS for the business card

Small written, can be anywhere.

Target Market(s)

Medical Professionals- Specialist doctors, Surgeons

Industry/Entity Type

Business

Requirements
Must have
• Must incorporate a medical logo (cross or Caduceus) in a smart way. We would like to see a corporate style logo that will attract to specialist doctors and surgeons.
Nice to have
• Would like to see a corporate style logo

```html
<!DOCTYPE html>
<html lang="en">
<head>
<meta charset="utf-8">
<title>Vantorel Private – Business Card</title>
<link href="https://fonts.googleapis.com/css2?family=Zilla+Slab:wght@300;400;600;700&display=swap" rel="stylesheet">
<style>
  :root {
    --stage: #000000;
    --paper: #ffffff;
    --green-deep: #073f22;
    --green-back: #0a4a29;
    --green-mid: #0f8b43;
    --green-bright: #23a650;
    --ink: #444444;
    --ink-dark: #2b2b2b;
    --navy: #1b2a4e;
    --badge: #4fb3e6;
  }
  * { margin: 0; padding: 0; box-sizing: border-box; }
  html, body { width: 969px; height: 1200px; overflow: hidden; background: var(--stage); }
  body { position: relative; font-family: "Zilla Slab", Georgia, serif; }

  .card { position: absolute; left: 99px; width: 741px; height: 424px; overflow: hidden; }
  .card--front { top: 172px; background: var(--paper); }
  .card--back { top: 621px; background: var(--green-back); }

  /* Front */
  .holder { position: absolute; left: 48px; top: 72px; color: var(--ink); font-weight: 300; font-size: 28px; line-height: 35px; }
  .address { position: absolute; left: 48px; top: 146px; color: var(--ink); font-size: 14px; line-height: 19.5px; }
  .contacts { position: absolute; left: 48px; top: 222px; list-style: none; color: var(--ink); font-size: 14px; line-height: 20px; }
  .contacts li { display: flex; align-items: center; gap: 8px; }
  .contacts svg { width: 14px; height: 14px; fill: var(--ink-dark); }

  .brand-mark { position: absolute; background: var(--green-mid); box-shadow: inset 0 0 0 7px var(--green-bright); }
  .card--front .brand-mark { left: 484px; top: 106px; width: 130px; height: 130px; }
  .brand-name { position: absolute; white-space: nowrap; text-align: center; font-weight: 400; }
  .card--front .brand-name { left: 403px; top: 265px; width: 279px; font-size: 34px; line-height: 40px; color: var(--green-deep); }

  .accreditation { position: absolute; left: 36px; top: 352px; display: flex; align-items: center; gap: 8px; }
  .accreditation__text { text-align: right; font-size: 13px; line-height: 17px; color: var(--navy); }
  .accreditation__text strong { font-weight: 600; }
  .accreditation__rule { width: 1px; height: 34px; background: var(--navy); }
  .accreditation__badge { display: flex; align-items: center; gap: 6px; font-size: 24px; color: var(--navy); }
  .accreditation__badge span { display: block; width: 24px; height: 24px; border-radius: 50%; background: var(--badge); }

  .licence { position: absolute; left: 354px; top: 351px; font-size: 12.5px; line-height: 18px; font-weight: 600; color: var(--ink-dark); white-space: nowrap; }

  .band { position: absolute; bottom: 0; height: 28px; }
  .band--dark { left: 0; width: 320px; background: var(--green-deep); }
  .band--light { left: 328px; right: 0; background: var(--green-mid); }

  /* Back */
  .card--back .brand-mark { left: 307px; top: 81px; width: 160px; height: 160px; }
  .card--back .brand-name { left: 77px; width: 582px; top: 288px; font-size: 46px; line-height: 56px; color: var(--paper); }
  .website { position: absolute; left: 90px; width: 582px; top: 362px; text-align: center; color: var(--paper); font-size: 18px; font-weight: 600; }
  .card--back .band--light { left: 0; right: auto; width: 561px; height: 27px; }
</style>
</head>
<body>

<section class="card card--front">
  <h1 class="holder">Daniel Ferrow<br>CEO</h1>
  <p class="address">Rua Monte Alvorada, nº214 – sala 502<br>Centro Clínico Aurora – Laranjeiras – Rio de Janeiro<br>CEP – 22240-117</p>
  <ul class="contacts">
    <li><svg viewBox="0 0 16 16" aria-hidden="true"><path d="M1 6c0-2 3-3 7-3s7 1 7 3v1h-3V5.5H4V7H1zM4 8h8l2 5H2z"/></svg>(21) 2718-4390</li>
    <li><svg viewBox="0 0 16 16" aria-hidden="true"><path d="M5 1h6v14H5zM6.2 2.5v5h3.6v-5z"/></svg>(21) 8362-1957 &nbsp;/ 9841-3075</li>
    <li><svg viewBox="0 0 16 16" aria-hidden="true"><path d="M1 3h14v10H1zM2.5 4.5v7h11v-7L8 9z" fill-rule="evenodd"/></svg>danielF@vantorelprivate.com</li>
  </ul>

  <div class="brand-mark"></div>
  <p class="brand-name">Vantorel Private</p>

  <div class="accreditation">
    <p class="accreditation__text">Accredited by<br><strong>QBL Financial Planning</strong></p>
    <div class="accreditation__rule"></div>
    <div class="accreditation__badge">QBL<span></span></div>
  </div>
  <p class="licence">Vantorel Private capital Authorised Representative of<br>QBL Asset Advisory Pty Ltd AFS Licensee no. 418593</p>

  <div class="band band--dark"></div>
  <div class="band band--light"></div>
</section>

<section class="card card--back">
  <div class="brand-mark"></div>
  <p class="brand-name">Vantorel Private</p>
  <p class="website">www.vantorelprivate.com</p>
  <div class="band band--light"></div>
</section>

</body>
</html>
```